Meridale Hair Studio Needs a new appointment business card

We need a new appointment card for our hair salon.

I Dont want bright out there colours.
I would like it to be neat, clean, easy to read. White, Black, with a hint of colour if needed.

We need
-Logo
-Phone number 47260385
-Mobile Number: 0417360528
Address: Shop 3/217 Tarrow Street, Kelby Court, Mackay 4740

BACK SIDE OF CARD
- Appointment Time & Date (White background so we are able to write on it)
(If you are unable to make your appointment please contact us ASAP 47260385)

I also would like the chatterly and Snapfold logo(Find us on Chatterly)(find us on Snapfold)

Target Market(s)

appointment card simple to read. all information for their next appoint For all our clients male and female

Industry/Entity Type

Hairdresser

Contact Information for Business Card

-Logo
-Phone number 47260385

BACK SIDE OF CARD

Font styles to use
Serif
Sans Serif
Script

Requirements
Must have
• White Back ground on backside with appointment deatils so we are able to write information (like appointment time and date)
Nice to have
• Find us on Chatterly
and
snapfold - meridale_hairstudio
Should not have
• BRIGHT COLOURS

```html
<!DOCTYPE html>
<html lang="en">
<head>
<meta charset="utf-8">
<title>Meridale Hair Studio – Appointment Card</title>
<link rel="stylesheet" href="https://fonts.googleapis.com/css2?family=Poppins:wght@400;500&family=Open+Sans:ital,wght@0,400;0,600;1,400&display=swap">
<style>
  :root {
    --page: #e9e9e9;
    --card: #ffffff;
    --ink: #111111;
    --ink-soft: #4a4a4a;
    --rule: #222222;
  }
  * { margin: 0; padding: 0; box-sizing: border-box; }
  html, body { width: 1200px; height: 1200px; overflow: hidden; }
  body { background: var(--page); position: relative; font-family: "Poppins", sans-serif; color: var(--ink); }

  .card {
    position: absolute;
    left: 257px;
    width: 686px;
    height: 392px;
    background: var(--card);
    border-radius: 26px;
  }
  .card--front { top: 160px; }
  .card--back  { top: 650px; font-family: "Open Sans", sans-serif; }
  .card > * { position: absolute; }

  /* Front */
  .brand-name {
    left: 0; width: 100%; top: 116px;
    text-align: center;
    font-family: "Poppins", sans-serif;
    font-weight: 500;
    font-size: 46px; line-height: 1;
    letter-spacing: 2px;
    color: var(--ink);
  }
  .brand-tagline {
    left: 0; width: 100%; top: 172px;
    text-align: center;
    font-family: "Poppins", sans-serif;
    font-size: 16px; letter-spacing: 5px;
    color: var(--ink);
  }
  .person {
    right: 354px; top: 245px;
    text-align: right;
  }
  .person__name { font-size: 22px; font-weight: 500; line-height: 28px; letter-spacing: 0.3px; }
  .person__role { font-size: 16px; line-height: 20px; }
  .person__address { font-size: 16px; line-height: 19px; color: var(--ink-soft); margin-top: 5px; letter-spacing: 0.2px; }

  .divider { left: 349px; top: 251px; width: 1.5px; height: 81px; background: var(--rule); }

  .contacts { left: 366px; top: 248px; list-style: none; }
  .contacts li { display: flex; align-items: center; height: 19.6px; font-size: 16px; color: var(--ink-soft); letter-spacing: 0.2px; }
  .contacts svg { width: 13px; height: 13px; margin-right: 9px; fill: var(--ink); flex: none; }

  /* Back */
  .appt-title { left: 0; width: 100%; top: 34px; text-align: center; font-size: 26px; font-weight: 600; }
  .fill-line { border-bottom: 1.5px dotted #555; height: 0; }
  .client-line { left: 48px; top: 125px; width: 401px; }
  .client-label { left: 458px; top: 103px; font-size: 18.5px; }
  .field-label { top: 173px; font-size: 21px; }
  .date-label { left: 41px; }
  .date-line { left: 108px; top: 195px; width: 260px; }
  .time-label { left: 390px; }
  .time-line { left: 449px; top: 195px; width: 133px; }
  .ampm { left: 589px; top: 179px; font-size: 15px; }

  .day { top: 250px; display: flex; align-items: center; font-size: 17.5px; }
  .day__box { width: 19px; height: 16px; border: 1.5px solid #333; margin-left: 9px; }

  .note { left: 0; width: 100%; top: 336px; text-align: center; font-size: 15px; font-style: italic; color: var(--ink-soft); }
</style>
</head>
<body>

<section class="card card--front" aria-label="Business card front">
  <div class="brand-name">MERIDALE</div>
  <div class="brand-tagline">HAIR-STUDIO</div>

  <div class="person">
    <div class="person__name">DANIEL HARTLEY</div>
    <div class="person__role">President</div>
    <div class="person__address">Shop 3/217 Tarrow Street<br>Kelby Court, Mackay 4740</div>
  </div>

  <div class="divider"></div>

  <ul class="contacts">
    <li><svg viewBox="0 0 24 24"><path d="M6.6 10.8a15.5 15.5 0 0 0 6.6 6.6l2.2-2.2a1 1 0 0 1 1-.25 11.4 11.4 0 0 0 3.6.57 1 1 0 0 1 1 1V20a1 1 0 0 1-1 1A17 17 0 0 1 3 4a1 1 0 0 1 1-1h3.5a1 1 0 0 1 1 1c0 1.250.2 2.450.57 3.6a1 1 0 0 1-.25 1z"/></svg>47260385</li>
    <li><svg viewBox="0 0 24 24"><path d="M7 1h10a2 2 0 0 1 2 2v18a2 2 0 0 1-2 2H7a2 2 0 0 1-2-2V3a2 2 0 0 1 2-2zm1 3v14h8V4z"/></svg>0417360528</li>
    <li><svg viewBox="0 0 24 24"><path d="M2 5h20v14H2zm2 2v.5l8 5 8-5V7z"/></svg>info@meridalehair.com</li>
    <li><svg viewBox="0 0 24 24"><path d="M12 2a10 10 0 1 0 0 20 10 10 0 0 0 0-20zm-1 17.9A8 8 0 0 1 4.2 10L9 14.8V16a2 2 0 0 0 2 2zm6.9-2.5A2 2 0 0 0 16 16h-1v-3a1 1 0 0 0-1-1H8v-2h2a1 1 0 0 0 1-1V7h2a2 2 0 0 0 2-2v-.4a8 8 0 0 1 2.9 12.8z"/></svg>www.meridalehair.com</li>
  </ul>
</section>

<section class="card card--back" aria-label="Business card back">
  <h1 class="appt-title">Next Appointment</h1>

  <div class="fill-line client-line"></div>
  <div class="client-label">has an appointment</div>

  <div class="field-label date-label">Date :</div>
  <div class="fill-line date-line"></div>
  <div class="field-label time-label">Time :</div>
  <div class="fill-line time-line"></div>
  <div class="ampm">AM/PM</div>

  <div class="day" style="left:46px">Sun<span class="day__box"></span></div>
  <div class="day" style="left:134px">Mon<span class="day__box"></span></div>
  <div class="day" style="left:227px">Tue<span class="day__box"></span></div>
  <div class="day" style="left:326px">Wed<span class="day__box"></span></div>
  <div class="day" style="left:419px">Thu<span class="day__box" style="margin-left:2px"></span></div>
  <div class="day" style="left:514px">Fri<span class="day__box" style="margin-left:2px"></span></div>
  <div class="day" style="left:587px">Sat<span class="day__box" style="margin-left:8px"></span></div>

  <p class="note">If you are unable to make your appointment please contact us ASAP 47260385)</p>
</section>

</body>
</html>
```